Progressive/contemporary business card design for successful Startups as a Service Company

New logo launched in 2020. New website launched in 2021. Now that COVID is (mostly) behind us, I'm networking with more people and need a business card that matches the company/logo design aesthetic.

```html
<!DOCTYPE html>
<html lang="en">
<head>
<meta charset="utf-8">
<title>Northstep — Business Card</title>
<link rel="stylesheet" href="https://fonts.googleapis.com/css2?family=Montserrat:wght@400;500;700&display=swap">
<style>
  :root {
    --backdrop: #c9c9cb;
    --paper: #f4f4f6;
    --ink-navy: #243650;
    --ink-grey: #8a8d93;
    --tone-green: #4fae3a;
    --tone-lime: #9dc52b;
    --tone-magenta: #d6067e;
    --tone-purple: #7f1f7e;
    --tone-blue: #1597d8;
    --tone-red: #e3261c;
    --tone-orange: #f39a12;
  }
  * { box-sizing: border-box; margin: 0; padding: 0; }
  html, body { width: 1200px; height: 800px; overflow: hidden; }
  body {
    background: var(--backdrop);
    font-family: "Montserrat", sans-serif;
    display: flex;
    align-items: center;
    justify-content: center;
    gap: 40px;
  }
  .card {
    position: relative;
    width: 540px;
    height: 309px;
    background: var(--paper);
    overflow: hidden;
    box-shadow: 0 10px 24px rgba(0,0,0,0.18);
  }
  .pattern-band {
    position: absolute;
    top: 0;
    height: 100%;
    background: linear-gradient(160deg,
      var(--tone-green) 0%, var(--tone-lime) 14%,
      var(--tone-magenta) 28%, var(--tone-blue) 44%,
      var(--tone-red) 58%, var(--tone-orange) 68%,
      var(--tone-purple) 82%, var(--tone-magenta) 100%);
  }
  .card--info .pattern-band {
    right: 0;
    width: 250px;
    clip-path: polygon(38% 0, 100% 0, 100% 100%, 0 100%);
  }
  .card--brand .pattern-band {
    left: 0;
    width: 250px;
    clip-path: polygon(0 0, 100% 0, 62% 100%, 0 100%);
  }
  .contact {
    position: absolute;
    left: 38px;
    top: 78px;
  }
  .contact__name {
    font-weight: 700;
    font-size: 19px;
    letter-spacing: 0.5px;
    color: var(--ink-navy);
    text-transform: uppercase;
  }
  .contact__role {
    font-size: 12px;
    color: var(--ink-grey);
    margin-top: 3px;
  }
  .contact__address {
    font-size: 11.5px;
    color: var(--ink-grey);
    line-height: 1.5;
    margin-top: 16px;
    font-style: normal;
  }
  .contact__list {
    list-style: none;
    margin-top: 12px;
    font-size: 11.5px;
    color: var(--ink-grey);
  }
  .contact__list li {
    display: flex;
    align-items: center;
    gap: 8px;
    line-height: 1.6;
  }
  .contact__list svg { width: 11px; height: 11px; fill: var(--ink-grey); }
  .wordmark {
    position: absolute;
    right: 46px;
    top: 50%;
    transform: translateY(-50%);
    display: flex;
    align-items: center;
    gap: 12px;
    font-weight: 500;
    font-size: 30px;
    letter-spacing: 6px;
    color: var(--ink-navy);
    text-transform: uppercase;
  }
  .wordmark__dot {
    width: 16px;
    height: 16px;
    border-radius: 50%;
    background: var(--tone-magenta);
  }
</style>
</head>
<body>
  <section class="card card--info" aria-label="Business card, contact side">
    <div class="contact">
      <h1 class="contact__name">Daniel Reyes</h1>
      <p class="contact__role">President</p>
      <address class="contact__address">1420 Alder Street<br>Portland, Oregon 97201</address>
      <ul class="contact__list">
        <li><svg viewBox="0 0 24 24" aria-hidden="true"><path d="M6.6 10.8a15.1 15.1 0 0 0 6.6 6.6l2.2-2.2a1 1 0 0 1 1-.25 11.4 11.4 0 0 0 3.6.57 1 1 0 0 1 1 1V20a1 1 0 0 1-1 1A17 17 0 0 1 3 4a1 1 0 0 1 1-1h3.5a1 1 0 0 1 1 1c0 1.25.2 2.45.57 3.57a1 1 0 0 1-.25 1z"/></svg>555-014-2290</li>
        <li><svg viewBox="0 0 24 24" aria-hidden="true"><path d="M2 5h20v14H2z M2 5l10 8 10-8" /></svg>reyes@northstep.co</li>
        <li><svg viewBox="0 0 24 24" aria-hidden="true"><circle cx="12" cy="12" r="10"/></svg>www.northstep.co</li>
      </ul>
    </div>
    <div class="pattern-band" role="img" aria-label="Diagonal band of colourful faceted triangle mosaic in green, magenta, blue, red and orange"></div>
  </section>

  <section class="card card--brand" aria-label="Business card, brand side">
    <div class="pattern-band" role="img" aria-label="Diagonal band of colourful faceted triangle mosaic in green, magenta, blue, red and orange"></div>
    <div class="wordmark">
      <span class="wordmark__name">Northstep</span>
      <span class="wordmark__dot" aria-hidden="true"></span>
    </div>
  </section>
</body>
</html>
```